GHollis Busisness Card

I am an aerospace consultant and at this time only need business cards.

Industry/Entity Type

Business

Contact Information for Business Card

Hollis Partners,LLC
Gerald T. Hollis

348 Birch Hollow Road
Madison AL 35762

256-555-0148 (cell)
256-555-0173 (fax)

geraldhollis@mailbrook.net

```html
<!DOCTYPE html>
<html lang="en">
<head>
<meta charset="utf-8">
<title>Hollis Partners, LLC – Business Card</title>
<link rel="stylesheet" href="https://fonts.googleapis.com/css2?family=Exo+2:wght@400;600&display=swap">
<style>
  :root {
    --page-bg: #e4e5e8;
    --card-white: #ffffff;
    --brand-red: #c9202f;
    --band-navy: #1c3a68;
    --name-light: #e3e7ee;
    --label-grey: #8a8d93;
  }
  * { box-sizing: border-box; margin: 0; padding: 0; }
  html, body {
    width: 1200px; height: 871px; overflow: hidden;
    background: var(--page-bg);
    font-family: "Exo 2", sans-serif;
  }
  .card {
    position: absolute; left: 100px; top: 150px;
    width: 1000px; height: 571px;
    background: var(--card-white);
    box-shadow: 0 6px 24px rgba(0,0,0,.12);
    overflow: hidden;
  }
  .brand {
    position: absolute; left: 70px; top: 62px;
    display: flex; align-items: center; gap: 18px;
  }
  .brand-mark { width: 40px; height: 40px; background: var(--brand-red); }
  .brand-name {
    color: var(--brand-red); font-weight: 600; font-size: 44px; letter-spacing: .5px;
  }
  .name-band {
    position: absolute; left: 0; top: 175px; width: 100%; height: 165px;
    background: var(--band-navy);
  }
  .person-name {
    position: absolute; right: 70px; bottom: 30px;
    color: var(--name-light); font-size: 44px; font-weight: 400; letter-spacing: 1px;
  }
  .contact {
    position: absolute; left: 70px; top: 378px;
    display: grid; grid-template-columns: 110px auto; row-gap: 6px;
    font-size: 26px; line-height: 34px;
  }
  .contact dt { color: var(--label-grey); }
  .contact dd { color: var(--brand-red); letter-spacing: .5px; }
  .address {
    position: absolute; right: 70px; top: 390px;
    text-align: right; color: var(--brand-red);
    font-size: 30px; line-height: 40px; font-style: normal; letter-spacing: .5px;
  }
</style>
</head>
<body>
  <article class="card">
    <header class="brand">
      <span class="brand-mark"></span>
      <span class="brand-name">Hollis Partners,LLC</span>
    </header>
    <section class="name-band">
      <h1 class="person-name">Gerald T. Hollis</h1>
    </section>
    <dl class="contact">
      <dt>Phone:</dt><dd>256-555-0148</dd>
      <dt>Fax:</dt><dd>256-555-0173</dd>
      <dt>Email:</dt><dd>geraldhollis@mailbrook.net</dd>
    </dl>
    <address class="address">
      348 Birch Hollow Road<br>
      Madison<br>
      AL 35762
    </address>
  </article>
</body>
</html>
```